Freelance Writer Letterhead Design

I need business letterhead designed for my freelance public relations/writing company in Denver, Colorado. I write and create articles, white papers, blogs and enewsletters for trade associations, health care organizations and foundations. I already have three versions of my logo in three colors. I would like the design to be executed in the three different colors, so I can use them in various ways. The final design should communicate professionalism, creativity and intellectual work. I want clients to think, "She is smart, professional, creative and more polished than the typical freelance writer; she looks like an agency, but is an individual."

Target Market(s)

Healthcare consulting firms, Foundations,

Industry/Entity Type

Communications

Font styles to use
Other font styles liked:
• Avenir.ttc and Outage.ttf are used in the logo

Requirements
Must have
• The logo
• I'd like it also to have as part of the design, these elements:
• Address: 4870 E. Wilmot Lane, #315, Pinecrest, CO 80417
• Website: www.quillharborwriting.com
• contact information: meredith@quillharborwriting.com
• phone: 303-918-2064
Nice to have
• a band of color at the bottom or along the sides, using the logo colors

```html
<!DOCTYPE html>
<html lang="en">
<head>
<meta charset="utf-8">
<title>Quill Harbor Writing — Letterhead Set</title>
<link rel="stylesheet" href="https://fonts.googleapis.com/css2?family=Mulish:wght@400;600;800&display=swap">
<style>
  :root {
    --backdrop: #efefef;
    --paper: #ffffff;
    --paper-edge: #dcdcdc;
    --ink: #333333;
    --faint: #f0f0f0;
    --orange: #f7931e;
    --green: #6dbe45;
    --blue: #2b7bc0;
  }
  * { margin: 0; padding: 0; box-sizing: border-box; }
  html, body { width: 1200px; height: 1000px; overflow: hidden; }
  body {
    background: var(--backdrop);
    font-family: "Mulish", "Avenir", sans-serif;
    color: var(--ink);
    position: relative;
  }
  .icon-defs { position: absolute; width: 0; height: 0; }

  .sheet {
    position: absolute;
    width: 392px;
    height: 506px;
    background: var(--paper);
    border: 1px solid var(--paper-edge);
    overflow: hidden;
  }
  .sheet--orange { left: 99px;  top: 77px;  --accent: var(--orange); z-index: 1; }
  .sheet--green  { left: 404px; top: 246px; --accent: var(--green);  z-index: 2; }
  .sheet--blue   { left: 706px; top: 412px; --accent: var(--blue);   z-index: 3; }

  .masthead {
    position: absolute;
    left: 41px; right: 41px; top: 21px;
    height: 42px;
    display: flex;
    align-items: center;
    gap: 10px;
  }
  .masthead__rule { flex: 1; height: 1.5px; background: var(--accent); }
  .wordmark { display: flex; align-items: center; gap: 6px; }
  .wordmark__circle {
    width: 42px; height: 42px;
    border: 3px solid var(--accent);
    border-radius: 50%;
  }
  .wordmark__name {
    color: var(--accent);
    font-weight: 800;
    line-height: 1;
  }
  .wordmark__name .line1 { display: block; font-size: 19px; letter-spacing: 0.5px; text-transform: uppercase; }
  .wordmark__name .line2 { display: block; font-size: 11px; margin-top: 2px; }

  .backdrop-circle {
    position: absolute;
    left: 50%; top: 251px;
    width: 134px; height: 134px;
    margin-left: -67px; margin-top: -67px;
    border: 6px solid var(--faint);
    border-radius: 50%;
  }

  .footer {
    position: absolute;
    left: 41px; right: 41px; top: 463px;
    border-top: 1.5px solid var(--accent);
    padding-top: 6px;
    font-size: 7.4px;
    line-height: 11px;
    white-space: nowrap;
  }
  .footer__row { display: flex; gap: 12px; }
  .footer__row--top { justify-content: center; }
  .footer__row--bottom { justify-content: space-between; }
  .contact { display: inline-flex; align-items: center; gap: 3px; }
  .contact svg { width: 7px; height: 7px; fill: var(--accent); }
</style>
</head>
<body>

<svg class="icon-defs" aria-hidden="true">
  <symbol id="icon-phone" viewBox="0 0 10 10"><rect x="2.5" y="0.5" width="5" height="9" rx="1"/></symbol>
  <symbol id="icon-mail" viewBox="0 0 10 10"><rect x="0" y="2" width="10" height="6" rx="0.5"/></symbol>
  <symbol id="icon-globe" viewBox="0 0 10 10"><circle cx="5" cy="5" r="4.5"/></symbol>
  <symbol id="icon-pin" viewBox="0 0 10 10"><path d="M5 0a3.5 3.5 0 0 1 3.5 3.5C8.5 6 5 10 5 10S1.5 6 1.5 3.5A3.5 3.5 0 0 1 5 0z"/></symbol>
</svg>

<section class="sheet sheet--orange" aria-label="Letterhead, orange version">
  <header class="masthead">
    <span class="masthead__rule"></span>
    <div class="wordmark">
      <span class="wordmark__circle"></span>
      <span class="wordmark__name"><span class="line1">Quill Harbor</span><span class="line2">writing</span></span>
    </div>
    <span class="masthead__rule"></span>
  </header>
  <div class="backdrop-circle"></div>
  <footer class="footer">
    <div class="footer__row footer__row--top">
      <span class="contact"><svg><use href="#icon-phone"/></svg>303 918 2064</span>
      <span class="contact"><svg><use href="#icon-mail"/></svg>meredith@quillharborwriting.com</span>
    </div>
    <div class="footer__row footer__row--bottom">
      <span class="contact"><svg><use href="#icon-globe"/></svg>www.quillharborwriting.com</span>
      <span class="contact"><svg><use href="#icon-pin"/></svg>4870 E. Wilmot Lane, #315, Pinecrest, CO 80417</span>
    </div>
  </footer>
</section>

<section class="sheet sheet--green" aria-label="Letterhead, green version">
  <header class="masthead">
    <span class="masthead__rule"></span>
    <div class="wordmark">
      <span class="wordmark__circle"></span>
      <span class="wordmark__name"><span class="line1">Quill Harbor</span><span class="line2">writing</span></span>
    </div>
    <span class="masthead__rule"></span>
  </header>
  <div class="backdrop-circle"></div>
  <footer class="footer">
    <div class="footer__row footer__row--top">
      <span class="contact"><svg><use href="#icon-phone"/></svg>303 918 2064</span>
      <span class="contact"><svg><use href="#icon-mail"/></svg>meredith@quillharborwriting.com</span>
    </div>
    <div class="footer__row footer__row--bottom">
      <span class="contact"><svg><use href="#icon-globe"/></svg>www.quillharborwriting.com</span>
      <span class="contact"><svg><use href="#icon-pin"/></svg>4870 E. Wilmot Lane, #315, Pinecrest, CO 80417</span>
    </div>
  </footer>
</section>

<section class="sheet sheet--blue" aria-label="Letterhead, blue version">
  <header class="masthead">
    <span class="masthead__rule"></span>
    <div class="wordmark">
      <span class="wordmark__circle"></span>
      <span class="wordmark__name"><span class="line1">Quill Harbor</span><span class="line2">writing</span></span>
    </div>
    <span class="masthead__rule"></span>
  </header>
  <div class="backdrop-circle"></div>
  <footer class="footer">
    <div class="footer__row footer__row--top">
      <span class="contact"><svg><use href="#icon-phone"/></svg>303 918 2064</span>
      <span class="contact"><svg><use href="#icon-mail"/></svg>meredith@quillharborwriting.com</span>
    </div>
    <div class="footer__row footer__row--bottom">
      <span class="contact"><svg><use href="#icon-globe"/></svg>www.quillharborwriting.com</span>
      <span class="contact"><svg><use href="#icon-pin"/></svg>4870 E. Wilmot Lane, #315, Pinecrest, CO 80417</span>
    </div>
  </footer>
</section>

</body>
</html>
```